Dental Learning Allies Needs a Great Looking Sales Brochure!

Please help us design a brochure for our company, Dental Learning Allies, LLC to use for sales and prospecting!
It is our first brochure, and as we are a small company, we don't normally use them, but we have an upcoming meeting and need a GREAT looking brochure with a call to action!
In addition to a pdf print ready version of the file, we need to receive a version with editable pdf text fields.
Our original thought is a 1-page, 4-panel fold or Tri-fold brochure, but we are open to recommendations based on the content.
More about us: We are a small company specializing in education, motivational speaking and event services for dental practices both large and big dental groups. You can check out our website at https://dentallearningallies.example
I have uploaded our logo files, some images for consideration, and proposed text content for the brochure. Note - if you have the space to add our RVX TOLM provider approval we would like to. If you do use the RVX Tolm logo, we need to follow their logo guidelines which are also attached.
Should you have any questions, please don't hesitate to ask!
Thank you for helping make us look great!!!!

Target Market(s)

Dental Support Organizations (DSO's)

Font styles to use
Serif
Sans Serif

Requirements
Must have
• Our company logo
• At least 1-2 photos
• Professional look and feel
• Text from uploaded word document for proposed copy
Nice to have
• RVX logo and language showing we are RVX TOLM provider

```html
<!DOCTYPE html>
<html lang="en">
<head>
<meta charset="utf-8">
<title>Dental Learning Allies – Sales Brochure</title>
<link href="https://fonts.googleapis.com/css2?family=Roboto+Condensed:wght@300;400;700&family=Tinos&display=swap" rel="stylesheet">
<style>
  :root{
    --blue:#1b6fc2;
    --black:#0b0b0b;
    --white:#ffffff;
    --ink:#333333;
    --grey:#8a8f96;
    --page:#f1f2f4;
    --photo-teeth:linear-gradient(135deg,#e9d7d3,#b9585a 60%,#f0e8e6);
    --photo-man:linear-gradient(160deg,#eef1f4,#b8c3cf 55%,#5d6f86);
    --photo-team:linear-gradient(120deg,#dfe6ee,#9fb3c8 50%,#eef2f6);
    --photo-class:linear-gradient(110deg,#e6eaf0,#b9c4d1 45%,#f3f5f8);
  }
  *{box-sizing:border-box;margin:0;padding:0}
  html,body{width:1200px;height:851px;overflow:hidden;background:var(--page)}
  body{position:relative;font-family:"Roboto Condensed",sans-serif;color:var(--ink)}
  .spread{position:absolute;top:205px;width:570px;height:440px;background:var(--white);box-shadow:0 2px 8px rgba(0,0,0,.18);overflow:hidden}
  .spread--outside{left:20px}
  .spread--inside{left:610px}
  .shapes{position:absolute;inset:0}
  .photo{position:absolute}
  .logo{position:absolute;display:flex;align-items:center;gap:6px;font-family:"Roboto Condensed",sans-serif;font-weight:400;text-transform:uppercase;letter-spacing:.5px;line-height:1.05}
  .logo__mark{width:12px;height:12px;flex:none}
  .logo--header{left:390px;top:22px;color:var(--white);font-size:15px}
  .logo--header .logo__mark{background:var(--white)}
  .logo--contact{left:215px;top:155px;color:var(--blue);font-size:13px}
  .logo--contact .logo__mark{background:var(--black)}
  .services-title{position:absolute;left:12px;top:116px;color:var(--white);font-size:24px;font-weight:400}
  .services-list{position:absolute;left:16px;top:170px;list-style:none;font-weight:300;font-size:12.5px;color:#555}
  .services-list li{margin-bottom:9.5px}
  .services-list li::before{content:"•";color:var(--ink);margin-right:5px}
  .contact{position:absolute;left:200px;top:192px;width:180px;text-align:center;font-size:9.5px;color:var(--ink)}
  .contact__label{font-weight:300;margin-bottom:10px}
  .contact__name{font-size:11px;font-weight:400;color:var(--black)}
  .contact__line{font-weight:300;line-height:1.2}
  .contact__person{margin-bottom:12px}
  .tagline{position:absolute;left:385px;top:352px;width:180px;text-align:center;font-family:"Tinos",serif;color:#444;text-transform:uppercase;line-height:.95}
  .tagline__big{font-size:19px}
  .tagline__small{font-size:10px}
  .badge{position:absolute;left:18px;top:102px;width:62px;height:52px;border:3px solid var(--white);border-radius:6px}
  .badge-caption{position:absolute;left:88px;top:100px;width:100px;color:var(--white);font-weight:700;font-size:27px;line-height:1}
  .badge-caption small{display:block;font-size:8.5px;line-height:1.05;text-transform:uppercase}
  .approval{position:absolute;left:200px;top:60px;width:178px;font-size:7.6px;font-weight:300;color:var(--white);line-height:1.42;text-align:justify}
  .why-title{position:absolute;left:383px;top:19px;width:187px;height:30px;padding-left:10px;display:flex;align-items:center;color:var(--white);font-size:16.5px}
  .why{position:absolute;left:393px;top:58px;width:170px;font-size:7.6px;font-weight:300;line-height:1.33;color:#444}
  .why h3{font-size:11px;font-weight:400;margin-bottom:6px;color:var(--ink)}
  .why ul{list-style:none;margin-bottom:9px}
  .why li{padding-left:6px;text-indent:-6px;margin-bottom:1.5px;text-align:justify}
  .why li::before{content:"• "}
  .why p{margin-bottom:9px;text-align:justify}
  .why .signature{line-height:1.25;text-align:left}
  .why .signature strong{font-weight:400}
</style>
</head>
<body>

<section class="spread spread--outside">
  <svg class="shapes" viewBox="0 0 570 440" aria-hidden="true">
    <rect x="0" y="0" width="377" height="5" fill="var(--black)"/>
    <polygon points="0,5 20,5 110,112 0,112" fill="var(--blue)"/>
    <polygon points="28,5 60,5 160,112 128,112" fill="var(--black)"/>
    <polygon points="70,5 187,5 187,60" fill="var(--blue)"/>
    <polygon points="0,112 125,112 143,140 0,140" fill="var(--black)"/>
    <polygon points="118,314 240,314 228,327 104,327" fill="var(--blue)"/>
    <rect x="377" y="0" width="193" height="75" fill="var(--blue)"/>
    <polygon points="377,330 470,330 455,344 377,344" fill="var(--black)"/>
    <polygon points="470,330 570,330 570,338 462,338" fill="var(--blue)"/>
    <polygon points="570,380 570,440 515,440" fill="var(--black)"/>
    <g stroke="#d7dde5" stroke-width="1">
      <line x1="385" y1="440" x2="420" y2="400"/><line x1="393" y1="440" x2="428" y2="400"/>
      <line x1="401" y1="440" x2="436" y2="400"/><line x1="409" y1="440" x2="444" y2="400"/>
    </g>
  </svg>
  <div class="photo" role="img" aria-label="Close-up photo of a smile with a dental mirror" style="left:187px;top:5px;width:190px;height:107px;background:var(--photo-teeth)"></div>
  <div class="photo" role="img" aria-label="Photo of a smiling business professional" style="left:377px;top:75px;width:193px;height:255px;background:var(--photo-man)"></div>
  <div class="photo" role="img" aria-label="Photo of a team meeting with a video call and charts" style="left:0;top:327px;width:377px;height:113px;background:var(--photo-team)"></div>

  <div class="logo logo--header"><span class="logo__mark"></span>Dental Learning<br>Allies</div>

  <h2 class="services-title">Services</h2>
  <ul class="services-list">
    <li>Clinical Training</li>
    <li>Web-Based Learning</li>
    <li>Chairside Coaching</li>
    <li>Train Your Trainer</li>
    <li>Regional or Annual Meetings</li>
    <li>Metric Analytics</li>
  </ul>

  <div class="logo logo--contact"><span class="logo__mark"></span>Dental Learning<br>Allies</div>
  <div class="contact">
    <p class="contact__label">Contact Us</p>
    <div class="contact__person">
      <p class="contact__name">Laura J. Benton</p>
      <p class="contact__line">(555) 201-4836</p>
      <p class="contact__line">laura@dentallearningallies.example</p>
    </div>
    <div class="contact__person">
      <p class="contact__name">Renee Calloway</p>
      <p class="contact__line">(555) 318-7724</p>
      <p class="contact__line">renee@dentallearningallies.example</p>
    </div>
  </div>

  <div class="tagline">
    <span class="tagline__big">Grow</span> <span class="tagline__small">your</span> <span class="tagline__big">DSO</span><br>
    <span class="tagline__small">with</span> <span class="tagline__big" style="font-size:14px">Customized</span><br>
    <span class="tagline__small" style="font-size:12px">Training</span><br>
    <span class="tagline__big" style="font-size:16px">Solutions</span>
  </div>
</section>

<section class="spread spread--inside">
  <svg class="shapes" viewBox="0 0 570 440" aria-hidden="true">
    <polygon points="0,80 75,5 110,5 0,115" fill="var(--blue)"/>
    <polygon points="0,125 120,5 150,5 0,155" fill="var(--black)"/>
    <polygon points="0,170 110,60 197,60 197,193 0,193" fill="var(--black)"/>
    <polygon points="150,5 200,5 200,51 105,51" fill="var(--blue)"/>
    <rect x="197" y="51" width="186" height="142" fill="var(--black)"/>
    <polygon points="60,180 383,180 383,193 48,193" fill="var(--blue)"/>
    <rect x="383" y="19" width="187" height="30" fill="var(--blue)"/>
    <polygon points="570,330 570,360 498,440 470,440" fill="var(--blue)"/>
    <polygon points="570,372 570,400 537,440 510,440" fill="var(--black)"/>
    <g stroke="#d7dde5" stroke-width="1">
      <line x1="440" y1="440" x2="500" y2="380"/><line x1="448" y1="440" x2="508" y2="380"/>
      <line x1="456" y1="440" x2="516" y2="380"/>
    </g>
  </svg>
  <div class="photo" role="img" aria-label="Photo of a group of dental staff in a training session" style="left:0;top:193px;width:383px;height:247px;background:var(--photo-class)"></div>

  <div class="badge" role="img" aria-label="Continuing education provider badge"></div>
  <div class="badge-caption">TOLM<small>Rural Vanguard Exchange<br>Approved Provider</small></div>

  <p class="approval">Dental Learning Allies, LLC is designated as an Approved TOLM Program Provider by the Rural Vanguard Exchange. The formal continuing education programs of this program provider are accepted by the RVX for Fellowship/Mastership and membership maintenance credit. Approval does not imply acceptance by a state or provincial board of dentistry or RVX endorsement. The current term of approval extends from 07/01/2017 to 06/30/2019. Provider ID #408152</p>

  <h2 class="why-title">Why partner with us?</h2>
  <div class="why">
    <h3>Do you want to:</h3>
    <ul>
      <li>Make hygiene the driver of every dental practice?</li>
      <li>Consistently achieve production goals?</li>
      <li>Provide excellent care for every patient in every practice?</li>
      <li>Provide continuity of care between providers?</li>
      <li>Standardize scripting to increase treatment enrollment?</li>
      <li>Improve the retention of both your staff and your patients?</li>
      <li>Supplement your education initiatives with metrics-based needs assessment?</li>
    </ul>
    <p>If you said yes to any of these questions, then DLA is right for you!</p>
    <p>“Dental Learning Allies delivered training for our team that isn’t offered anywhere else. Their training has dramatically changed our team’s ability to influence treatment acceptance. I would recommend their services to any DSO looking to increase profitability!”</p>
    <p class="signature"><strong>Dr. Martin Oakes,</strong><br>Chief Clinical Officer,<br>Bright Harbor Practice Group</p>
  </div>
</section>

</body>
</html>
```